Chinese Language Posters - TKUOME

We have created a series of African American heritage posters that will be distributed to Chinese Language Schools. We need a designer to create great posters for K-12 programs.

Quotes:
We have quotes from 6 important figures in Black History. We are seeking a designer to develop a poster utilizing at least one quote from each historical figure.

The designer MUST be fluent in Chinese in order to ensure the appropriate type and font.

Our organization, Tidewater Kestrel Union of Orchard Mentors Exchange, is a small organization of parents in the Bay Area working to encourage and support Black students learning the Chinese language.

Target Market(s)

These posters will be made available to Chinese Immersion schools (k-12).

Industry/Entity Type

Learning

Requirements
Must have
• Each poster should contain one quote from the list below.

Please create a poster of one historical figure and include their quote. The image can be abstract, landscape or an image of the figure.

The image should also include our logo. Our preferred logo is with the puffs but we understand if the clipart logo may be a better fit for the posters. (We LOVE the puffs logo though).
Nice to have
• I have uploaded images of each figure. The images can be used or a more abstract background. We are flexible. We would prefer a mix that includes figures and abstract backgrounds just focusing on the quote. We are open.

```html
<!DOCTYPE html>
<html lang="en">
<head>
<meta charset="utf-8">
<title>TKUOME Heritage Poster – Harlan Whitfield</title>
<link rel="stylesheet" href="https://fonts.googleapis.com/css2?family=Source+Sans+3:wght@400;600&family=Noto+Serif+SC:wght@400&family=Noto+Sans+SC:wght@400&display=swap">
<style>
  :root {
    --ink: #0d0d0d;
    --paper: #ffffff;
    --signal-red: #e1252b;
    --stage-center: #6a6a6a;
    --stage-edge: #000000;
    --photo-light: #e9e7e2;
    --photo-mid: #9a9894;
    --photo-dark: #5b5d60;
  }
  * { box-sizing: border-box; margin: 0; padding: 0; }
  html, body { width: 1200px; height: 999px; overflow: hidden; }
  body {
    position: relative;
    background: radial-gradient(ellipse 55% 75% at 50% 50%, var(--stage-center) 0%, #262626 55%, var(--stage-edge) 85%);
    font-family: "Source Sans 3", "Myriad Pro", Arial, sans-serif;
  }
  .poster {
    position: absolute;
    left: 256px; top: 13px;
    width: 688px; height: 972px;
    background: var(--paper);
    overflow: hidden;
  }
  .poster-shapes { position: absolute; inset: 0; }
  .brand {
    position: absolute;
    left: 0; right: 0; top: 68px;
    display: flex; align-items: center; justify-content: center; gap: 12px;
  }
  .brand-dot {
    width: 40px; height: 40px; border-radius: 50%;
    background: var(--signal-red);
  }
  .brand-text { display: flex; flex-direction: column; }
  .brand-name {
    font-weight: 400; font-size: 44px; line-height: 44px;
    color: var(--ink); letter-spacing: 0.5px;
  }
  .brand-tagline {
    font-size: 8px; line-height: 10px; color: var(--ink);
  }
  .portrait-frame {
    position: absolute;
    left: 16px; top: 147px;
    width: 658px; height: 497px;
    background: var(--ink);
    border-radius: 30px;
    padding: 12px;
  }
  .portrait-inner {
    width: 100%; height: 100%;
    background: var(--paper);
    border-radius: 20px;
    padding: 4px;
  }
  .portrait {
    width: 100%; height: 100%;
    border-radius: 16px;
    background: radial-gradient(ellipse 40% 55% at 52% 60%, var(--photo-mid) 0%, var(--photo-dark) 55%, transparent 56%),
                linear-gradient(180deg, var(--photo-light) 0%, #dcdad5 100%);
  }
  .name-en {
    position: absolute;
    left: 112px; top: 658px;
    font-size: 42px; font-weight: 400; line-height: 52px;
    color: var(--paper); letter-spacing: 0.3px;
  }
  .name-band {
    position: absolute;
    left: 0; top: 709px;
    width: 688px; height: 90px;
    background: var(--ink);
    display: flex; align-items: center; justify-content: center;
  }
  .name-zh {
    font-family: "Noto Serif SC", "Songti SC", serif;
    font-size: 50px; color: var(--paper); letter-spacing: 2px;
  }
  .quote-en {
    position: absolute;
    left: 48px; top: 812px;
    font-size: 34px; line-height: 44px; color: var(--ink);
  }
  .quote-zh {
    position: absolute;
    left: 396px; top: 818px;
    font-family: "Noto Sans SC", "PingFang SC", sans-serif;
    font-size: 30px; line-height: 46px; color: var(--ink);
    letter-spacing: 1px;
  }
  .footer-band {
    position: absolute;
    left: 0; bottom: 0;
    width: 688px; height: 39px;
    background: var(--signal-red);
  }
</style>
</head>
<body>
  <main class="poster">
    <svg class="poster-shapes" width="688" height="972" viewBox="0 0 688 972" aria-hidden="true">
      <polygon points="16,15 688,15 688,53 24,53" fill="var(--ink)"/>
      <polygon points="0,330 18,330 30,660 0,660" fill="var(--signal-red)"/>
      <polygon points="0,640 88,640 100,692 0,692" fill="var(--signal-red)"/>
      <polygon points="98,654 688,654 688,709 110,709" fill="var(--signal-red)"/>
      <rect x="0" y="692" width="104" height="17" fill="var(--signal-red)"/>
      <line x1="0" y1="695" x2="103" y2="695" stroke="var(--paper)" stroke-width="2"/>
    </svg>

    <header class="brand">
      <span class="brand-dot"></span>
      <div class="brand-text">
        <span class="brand-name">TKUOME</span>
        <span class="brand-tagline">Tidewater Kestrel Union of Orchard Mentors Exchange</span>
      </div>
    </header>

    <div class="portrait-frame">
      <div class="portrait-inner">
        <div class="portrait" role="img" aria-label="Portrait photograph of Harlan Whitfield in a grey suit and dark glasses against a pale wall"></div>
      </div>
    </div>

    <h1 class="name-en">HARLAN WHITFIELD</h1>
    <div class="name-band"><p class="name-zh">哈兰·惠特菲尔德</p></div>

    <p class="quote-en">What is the quality<br>of your intent?</p>
    <p class="quote-zh">你的意图真诚而<br>与人为善吗？</p>

    <div class="footer-band"></div>
  </main>
</body>
</html>
```